Medigap Insurance Interactive website

We are looking at redesigning our website for a more up to date and responsive look and feel. We will code this site using Bootstrap 3 so please research and know how to design for this. Attached is our logo and a wireframe for the new site.
I look forward to seeing what you guys can do.

Target Market(s)

People elegible for Medigap Insurance in the US

Industry/Entity Type

Insurance

Number of Pages Required

5+ page

Font styles to use
Sans Serif

Requirements
Must have
• Match the logo
• Be Bootstrap 3 compatible design
• Font Awesome Icons

```html
<!DOCTYPE html>
<html lang="en">
<head>
<meta charset="utf-8">
<title>Harborcare – Medicare Supplements</title>
<link rel="stylesheet" href="https://fonts.googleapis.com/css2?family=PT+Serif:wght@400;700&family=Open+Sans:wght@400;600;700&display=swap">
<style>
  :root{
    --red:#b52019;
    --navy:#0b2d69;
    --page:#f3f3f3;
    --white:#ffffff;
    --text:#333333;
    --rule:#dddddd;
    --footer:#9e9e9e;
    --serif:"PT Serif", Georgia, serif;
    --sans:"Open Sans", Arial, sans-serif;
  }
  *{box-sizing:border-box;margin:0;padding:0}
  html,body{width:1200px;height:1008px;overflow:hidden}
  body{background:var(--page);font-family:var(--sans);color:var(--text);position:relative}

  .topbar{position:absolute;left:0;top:0;width:1200px;height:47px;background:var(--red);color:var(--white)}
  .topbar__phone{position:absolute;left:606px;top:14px;display:flex;align-items:center;gap:10px;font-family:var(--serif);font-size:15.5px;letter-spacing:.2px}
  .topbar__social{position:absolute;left:932px;top:10px;display:flex;gap:4px}
  .topbar__social span{width:26px;height:26px;border:1.5px solid var(--white);border-radius:50%;display:block}

  .header{position:absolute;left:0;top:47px;width:1200px;height:76px;background:var(--white)}
  .brand{position:absolute;left:150px;top:30px;font-family:var(--serif);font-size:19px;color:var(--navy);letter-spacing:.5px;line-height:21px}
  .nav{position:absolute;top:34px;font-family:var(--serif);font-size:12.8px;color:var(--navy);white-space:nowrap}
  .nav--active{border-bottom:3px solid var(--navy);padding-bottom:4px}
  .nav-buy{position:absolute;left:962px;top:22px;width:88px;height:38px;background:var(--red);color:var(--white);font-family:var(--serif);font-size:12.8px;display:flex;align-items:center;justify-content:center}

  .hero-photo{position:absolute;top:123px;height:401px}
  .hero-photo--people{left:0;width:652px;background:linear-gradient(120deg,#6b5a48 0%,#a48d70 40%,#7a6652 70%,#3a322b 100%)}
  .hero-photo--pills{left:660px;width:540px;background:linear-gradient(135deg,#8d8e97 0%,#a9abb5 45%,#7d7f8a 100%)}
  .hero__title{position:absolute;left:150px;top:280px;font-family:var(--serif);font-size:28px;font-weight:400;color:var(--white)}
  .hero__lead{position:absolute;left:150px;top:323px;width:460px;font-size:14.6px;line-height:18px;color:var(--white)}
  .play{position:absolute;left:902px;top:273px}
  .play__label{position:absolute;left:832px;top:347px;width:200px;text-align:center;font-family:var(--serif);font-size:18px;color:var(--white)}

  .tabs{position:absolute;left:150px;top:550px;width:900px;height:77px;display:flex;gap:3.5px}
  .tab{flex:1;background:var(--white);border:1px solid var(--rule);border-bottom:3px solid var(--navy);display:flex;align-items:center;justify-content:center;font-family:var(--serif);font-size:19px;color:var(--navy)}
  .tab--active{background:var(--navy);color:var(--white);border-color:var(--navy)}

  .card{position:absolute;top:656px;height:238px;width:295px;background:var(--white);border:1px solid var(--rule);padding:30px 20px 0 20px}
  .card--about{left:150px}
  .card--quote{left:453px}
  .card--news{left:755px;background:var(--navy);border-color:var(--navy);color:var(--white)}
  .card__title{font-family:var(--serif);font-size:18.5px;font-weight:400;color:var(--navy);padding-bottom:14px;border-bottom:2px solid #e4e4e4}
  .card--news .card__title{color:var(--white);border-bottom-color:#2c4a85}
  .card__text{margin-top:15px;font-size:12.1px;line-height:14.6px}
  .btn-learn{position:absolute;left:20px;top:180px;width:100px;height:29px;background:var(--red);color:var(--white);font-size:12.6px;display:flex;align-items:center;justify-content:center}
  .quote__author{position:absolute;left:25px;top:185px;font-size:13.5px}
  .quote__mark{position:absolute;left:268px;top:202px;font-family:var(--serif);font-size:18px;color:#777;font-style:normal}
  .signup{position:absolute;left:23px;top:93px;display:flex}
  .signup__input{width:171px;height:34px;background:var(--white)}
  .signup__btn{width:85px;height:34px;background:var(--red);font-family:var(--serif);font-size:13.5px;display:flex;align-items:center;justify-content:center}
  .news__hint{position:absolute;left:22px;top:146px;width:250px;font-size:14px;line-height:17px}

  .footer{position:absolute;left:0;top:947px;width:1200px;height:61px;background:var(--footer);color:var(--white);font-size:13px}
  .footer__link{position:absolute;top:22px;white-space:nowrap}
  .footer__divider{position:absolute;left:450px;top:16px;width:1px;height:30px;background:var(--white)}
  .footer__call{position:absolute;left:466px;top:22px}
  .footer__copy{position:absolute;right:150px;top:22px}
</style>
</head>
<body>

<div class="topbar">
  <div class="topbar__phone">
    <svg width="10" height="16" viewBox="0 0 10 16"><rect x="1" y="1" width="8" height="14" rx="1.5" fill="none" stroke="#fff" stroke-width="1.5"/><line x1="4" y1="12.5" x2="6" y2="12.5" stroke="#fff" stroke-width="1.2"/></svg>
    <span>Compare Rates and Save &nbsp;(555) 210 3390</span>
  </div>
  <div class="topbar__social" aria-label="Social links">
    <span></span><span></span><span></span><span></span>
  </div>
</div>

<header class="header">
  <div class="brand">HARBORCARE</div>
  <a class="nav nav--active" style="left:322px">MEDICARE SUPPLIMENTS</a>
  <a class="nav" style="left:510px">PART D</a>
  <a class="nav" style="left:578px">HOW TO DECIDE</a>
  <a class="nav" style="left:707px">LEARN ONLINE</a>
  <a class="nav" style="left:830px">WHY HARBORCARE</a>
  <a class="nav-buy">BUY NOW</a>
</header>

<section>
  <div class="hero-photo hero-photo--people" role="img" aria-label="Photo of an older couple reviewing insurance papers with an advisor"></div>
  <h1 class="hero__title">Why Us</h1>
  <p class="hero__lead">Lorem ipsum dolor sit amet, adipisicing elit, sed do incididunt ut labore et dolore magna aliqua. Ut enim ad veniam ..</p>

  <div class="hero-photo hero-photo--pills" role="img" aria-label="Video still of white pills spilling from a bottle"></div>
  <svg class="play" width="64" height="64" viewBox="0 0 64 64"><circle cx="32" cy="32" r="32" fill="#e9e9ec"/><path d="M27 22 L42 32 L27 42 Z" fill="#6b6d76"/></svg>
  <div class="play__label">CLICK TO PLAY</div>
</section>

<nav class="tabs">
  <div class="tab tab--active">COMPARE RATES</div>
  <div class="tab">BUY NOW</div>
  <div class="tab">LEARN ONLINE.</div>
  <div class="tab">GET EXPERT HELP</div>
</nav>

<article class="card card--about">
  <h2 class="card__title">About Us</h2>
  <p class="card__text">Lorem ipsum dolor sit amet, adipisicing elit, sed do incididunt ut labore et dolore magna aliqua. Ut enim ad veniam, quis exercitation ullamco laboris nisi aliquip ex commodo consequat.</p>
  <a class="btn-learn">Learn More</a>
</article>

<article class="card card--quote">
  <h2 class="card__title">What People are Saying</h2>
  <p class="card__text">“Lorem ipsum dolor sit amet, adipisicing elit, sed do incididunt ut labore et dolore magna aliqua. Ut enim ad veniam, quis exercitation ullamco laboris nisi ”</p>
  <p class="quote__author">- Willow Harper</p>
  <i class="quote__mark">”</i>
</article>

<article class="card card--news">
  <h2 class="card__title">Monthly Updates</h2>
  <div class="signup"><div class="signup__input"></div><div class="signup__btn">Sign Up</div></div>
  <p class="news__hint">Enter email for customized monthly rate updates and more</p>
</article>

<footer class="footer">
  <span class="footer__link" style="left:149px">Harborcare</span>
  <span class="footer__link" style="left:234px">Sitemap</span>
  <span class="footer__link" style="left:295px">Buy Now</span>
  <span class="footer__link" style="left:361px">Blog</span>
  <span class="footer__link" style="left:401px">Login</span>
  <div class="footer__divider"></div>
  <div class="footer__call">Call us &nbsp;<b>(555) 210 3390</b></div>
  <div class="footer__copy">Copyright © 2016</div>
</footer>

</body>
</html>
```